Business Card Design

Vintage looking Hair Salon, where the customer service is 100%. We are based in a cottage. With shabby chic console tables and beautiful ornate mirrors..and rich brown leather cutting chairs. Chandeliers at the window, and a ornate patchwork sofa.
our clientele are 28years upwards.. Mums with small children.. Ladies that lunch, and men that want more than a barbers and are prepared to pay for our services.
I am looking for a classy business card.. That look expensive.. Where our initials WMP become a visual reference.. I was thinking of cream card initials in black on a embossed tarnished silver.. But I'm open to suggestion. I want,  need the design to be able to work with flyers price list ect.

Industry/Entity Type
Business
Contact Information for Business Card
Willow Mane Parlour
17 Fernbrook Lane
Dunmore Green
bN42 6QW
FB thewillowmaneparlour
Info@thewilowmaneparlour.co.uk
0208 761 5924

```html
<!DOCTYPE html>
<html lang="en">
<head>
<meta charset="utf-8">
<title>Willow Mane Parlour – Business Card</title>
<link rel="stylesheet" href="https://fonts.googleapis.com/css2?family=Open+Sans:wght@400;600&display=swap">
<style>
  :root {
    --backdrop: #4a3f39;
    --card: #111112;
    --ink: #f4f2ee;
    --seal: #3b3b3d;
  }
  html, body {
    margin: 0;
    padding: 0;
    overflow: hidden;
  }
  body {
    width: 1200px;
    height: 720px;
    background: var(--backdrop);
    position: relative;
    font-family: "Open Sans", sans-serif;
  }
  .business-card {
    position: absolute;
    left: 150px;
    top: 90px;
    width: 900px;
    height: 540px;
    background: var(--card);
    border-radius: 6px;
    color: var(--ink);
    text-align: center;
    box-sizing: border-box;
    padding-top: 70px;
  }
  .brand-seal {
    display: block;
    width: 120px;
    height: 120px;
    margin: 0 auto;
    border-radius: 50%;
    background: var(--seal);
  }
  .brand-name {
    margin: 22px 0 0;
    font-weight: 600;
    font-size: 50px;
    letter-spacing: 4px;
    text-transform: uppercase;
    line-height: 1.1;
  }
  .contact-list {
    list-style: none;
    margin: 44px 0 0;
    padding: 0;
    font-size: 22px;
    font-weight: 400;
    line-height: 1.3;
  }
  .contact-list li {
    margin-bottom: 10px;
  }
  .contact-icon {
    display: block;
    width: 20px;
    height: 16px;
    margin: 0 auto 4px;
  }
</style>
</head>
<body>
  <section class="business-card">
    <span class="brand-seal"></span>
    <h1 class="brand-name">Willow Mane Parlour</h1>
    <ul class="contact-list">
      <li class="contact-phone">
        <svg class="contact-icon" viewBox="0 0 20 16" aria-hidden="true">
          <path d="M2 6 C6 1 14 1 18 6 L15 8 L13 5 C11 4 9 4 7 5 L5 8 Z" fill="#f4f2ee"/>
        </svg>
        0208 761 5924
      </li>
      <li class="contact-email">
        <svg class="contact-icon" viewBox="0 0 20 16" aria-hidden="true">
          <rect x="1" y="2" width="18" height="12" fill="none" stroke="#f4f2ee" stroke-width="1.6"/>
          <path d="M1 2 L10 9 L19 2" fill="none" stroke="#f4f2ee" stroke-width="1.6"/>
        </svg>
        Info@thewilowmaneparlour.co.uk
      </li>
      <li class="contact-address">17 Fernbrook Lane Dunmore Green bN42 6QW FB</li>
    </ul>
  </section>
</body>
</html>
```